Membership Certificate for Chamber of Commerce Member

I am looking for a certificate to present to Chamber of Commerce Members that showcases their annual membership. The certificate will be placed in frame. I have attached a sample image of the frame from another Chamber of Commerce. I have also attached a proof of the frame that shows our logo at the top and the words "Working Together for a Stronger Community" at the bottom. The certificate should be 7" wide by 5" high. It should say Proud Chamber Member and the year, 2022. I have attached two versions of our logo. I am open to any further suggestions.

Target Market(s)

Business owners/managers

Requirements
Must have
• Year, Proud Chamber Member
Nice to have
• Colors and design that fit our logo and branding. Our website is www.thebrindlecrestchamber.com.

```html
<!DOCTYPE html>
<html lang="en">
<head>
<meta charset="utf-8">
<title>Certificate of Chamber Member 2022</title>
<link rel="stylesheet" href="https://fonts.googleapis.com/css2?family=Poppins:wght@600;800&family=Roboto+Condensed:wght@500;700&family=Kaushan+Script&display=swap">
<style>
  :root {
    --navy: #0f4a64;
    --orange: #f7931e;
    --green: #3cb54a;
    --cream: #efebe2;
    --paper: #ffffff;
    --ink: #0e4a63;
    --brand-blue: #2e3192;
  }
  * { margin: 0; padding: 0; box-sizing: border-box; }
  html, body {
    width: 1200px;
    height: 800px;
    overflow: hidden;
    background: var(--paper);
  }
  .certificate {
    position: relative;
    width: 1200px;
    height: 800px;
    background: var(--paper);
    overflow: hidden;
  }
  .chevrons {
    position: absolute;
    inset: 0;
  }
  .title-block {
    position: absolute;
    left: 72px;
    top: 58px;
    color: var(--ink);
    font-family: "Poppins", sans-serif;
    font-weight: 800;
    line-height: 1;
  }
  .title-main {
    font-size: 86px;
    letter-spacing: 1px;
  }
  .title-sub {
    margin-top: 2px;
    font-size: 37px;
    letter-spacing: 0.5px;
  }
  .chamber-name {
    position: absolute;
    left: 206px;
    top: 250px;
    width: 320px;
    display: flex;
    flex-direction: column;
    align-items: center;
    gap: 22px;
  }
  .chamber-mark {
    width: 200px;
    height: 200px;
    border-radius: 50%;
    background: var(--brand-blue);
  }
  .chamber-title {
    color: var(--brand-blue);
    font-family: "Poppins", sans-serif;
    font-weight: 600;
    font-size: 24px;
    line-height: 1.2;
    text-align: center;
  }
  .motto {
    position: absolute;
    left: 70px;
    top: 598px;
    color: var(--ink);
    font-family: "Kaushan Script", cursive;
    font-size: 52px;
    line-height: 84px;
  }
  .motto-line-1 { padding-left: 30px; }
  .seal {
    position: absolute;
    left: 650px;
    top: 245px;
    width: 380px;
    height: 380px;
  }
  .seal-text {
    font-family: "Roboto Condensed", sans-serif;
    fill: var(--paper);
    text-anchor: middle;
  }
  .seal-star {
    fill: var(--paper);
    font-family: sans-serif;
    font-size: 16px;
    text-anchor: middle;
  }
</style>
</head>
<body>
<main class="certificate">
  <svg class="chevrons" width="1200" height="800" viewBox="0 0 1200 800" aria-hidden="true">
    <polygon fill="var(--orange)" points="1040,0 1200,0 1050,300 1177,800 1017,800 890,300"/>
    <polygon fill="var(--navy)" points="895,0 985,0 860,250 1200,661 1200,770 770,250"/>
    <polygon fill="var(--navy)" points="1200,140 1088,370 1200,600"/>
  </svg>

  <header class="title-block">
    <div class="title-main">CERTIFICATE</div>
    <div class="title-sub">OF CHAMBER MEMBER 2022</div>
  </header>

  <div class="chamber-name">
    <span class="chamber-mark"></span>
    <span class="chamber-title">BRINDLECREST<br>CHAMBER OF COMMERCE<br>&amp; TOURISM</span>
  </div>

  <svg class="seal" viewBox="0 0 380 380" role="group" aria-label="Proud Chamber Member and the year, 2022">
    <g fill="var(--cream)">
      <circle cx="190" cy="190" r="168"/>
      <circle cx="190" cy="40" r="36"/><circle cx="265" cy="60" r="36"/>
      <circle cx="320" cy="115" r="36"/><circle cx="340" cy="190" r="36"/>
      <circle cx="320" cy="265" r="36"/><circle cx="265" cy="320" r="36"/>
      <circle cx="190" cy="340" r="36"/><circle cx="115" cy="320" r="36"/>
      <circle cx="60" cy="265" r="36"/><circle cx="40" cy="190" r="36"/>
      <circle cx="60" cy="115" r="36"/><circle cx="115" cy="60" r="36"/>
    </g>
    <g fill="var(--navy)">
      <circle cx="190" cy="190" r="160"/>
      <circle cx="190" cy="44" r="28"/><circle cx="263" cy="64" r="28"/>
      <circle cx="316" cy="117" r="28"/><circle cx="336" cy="190" r="28"/>
      <circle cx="316" cy="263" r="28"/><circle cx="263" cy="316" r="28"/>
      <circle cx="190" cy="336" r="28"/><circle cx="117" cy="316" r="28"/>
      <circle cx="64" cy="263" r="28"/><circle cx="44" cy="190" r="28"/>
      <circle cx="64" cy="117" r="28"/><circle cx="117" cy="64" r="28"/>
    </g>
    <circle cx="190" cy="190" r="134" fill="var(--paper)"/>
    <circle cx="190" cy="190" r="128" fill="var(--green)"/>
    <circle cx="190" cy="190" r="118" fill="none" stroke="var(--paper)" stroke-width="2"/>
    <g class="seal-text">
      <text x="190" y="128" font-size="30" font-weight="500">Proud</text>
      <text x="190" y="160" font-size="30" font-weight="500">Chamber</text>
      <text x="190" y="192" font-size="30" font-weight="500">Member</text>
      <text x="190" y="224" font-size="30" font-weight="500">and the year,</text>
      <text x="190" y="278" font-size="52" font-weight="700">2022</text>
    </g>
    <g class="seal-star">
      <text x="120" y="152">★</text><text x="116" y="184">★</text>
      <text x="258" y="124">★</text><text x="266" y="156">★</text><text x="260" y="186">★</text>
    </g>
  </svg>

  <p class="motto">
    <span class="motto-line-1">" Working Together</span><br>
    <span class="motto-line-2">for a Stronger Community"</span>
  </p>
</main>
</body>
</html>
```